Heating and Air Conditioning Company Needs a Business Card Design

Need a business card design for a company in South Carolina called "Larkfield Heating & Cooling LLC". We install, maintain, and repair HVAC systems and the bulk of our business is residential. We have a logo and are looking for a clean, professional looking card that resonates with "setting the standard for service and comfort".
Updates
Forgot to include this info - Licensed & Insured

Industry/Entity Type
Business

```html
<!DOCTYPE html>
<html lang="en">
<head>
<meta charset="utf-8">
<title>Larkfield Heating &amp; Cooling LLC – Business Card</title>
<link rel="stylesheet" href="https://fonts.googleapis.com/css2?family=Source+Sans+3:wght@400;600;700&display=swap">
<style>
  :root {
    --backdrop: #e7e4df;
    --card: #262626;
    --white: #ffffff;
    --text: #e6e6e6;
    --muted: #b9b9b9;
    --red: #e0262b;
    --blue: #1a63c6;
  }
  * { box-sizing: border-box; margin: 0; padding: 0; }
  html, body {
    width: 1200px; height: 1000px; overflow: hidden;
    background: var(--backdrop);
    font-family: "Source Sans 3", "Myriad Pro", sans-serif;
  }
  .card {
    position: absolute; left: 265px; width: 665px; height: 397px;
    background: var(--card);
    box-shadow: 0 6px 18px rgba(0,0,0,0.35);
  }
  .card-front { top: 73px; }
  .card-back { top: 532px; }

  .brand { position: absolute; display: flex; align-items: center; color: var(--white); font-weight: 700; white-space: nowrap; }
  .brand-dot { border-radius: 50%; background: var(--blue); flex: none; }
  .card-front .brand { left: 0; right: 0; top: 170px; justify-content: center; font-size: 36px; gap: 14px; }
  .card-front .brand-dot { width: 34px; height: 34px; }
  .card-back .brand { left: 33px; width: 310px; top: 182px; justify-content: center; font-size: 19px; gap: 8px; }
  .card-back .brand-dot { width: 18px; height: 18px; }

  .licence { position: absolute; left: 33px; width: 310px; top: 240px; text-align: center; color: var(--muted); font-size: 16px; }

  .contact-person { position: absolute; left: 374px; top: 44px; }
  .person-name { color: var(--red); font-size: 21px; font-weight: 600; line-height: 1.2; }
  .person-role { color: var(--text); font-size: 16px; line-height: 1.2; }

  .contact-list { position: absolute; left: 374px; top: 132px; list-style: none; }
  .contact-item { display: flex; align-items: flex-start; color: var(--text); font-size: 16px; line-height: 23px; margin-bottom: 1px; }
  .contact-item.gap { margin-top: 3px; }
  .contact-icon { width: 14px; height: 14px; margin: 5px 9px 0 0; flex: none; fill: var(--blue); }

  .services { position: absolute; left: 0; right: 0; top: 343px; text-align: center; color: var(--muted); font-size: 16px; }
</style>
</head>
<body>
  <section class="card card-front">
    <div class="brand"><span class="brand-dot"></span>Larkfield Heating &amp; Cooling LLC</div>
  </section>

  <section class="card card-back">
    <div class="brand"><span class="brand-dot"></span>Larkfield Heating &amp; Cooling LLC</div>
    <p class="licence">Licensed &amp; Insured</p>

    <div class="contact-person">
      <p class="person-name">Dale Whitmore</p>
      <p class="person-role">Certified Technician</p>
    </div>

    <ul class="contact-list">
      <li class="contact-item">
        <svg class="contact-icon" viewBox="0 0 14 14"><path d="M4 0h6a1 1 0 0 1 1 1v12a1 1 0 0 1-1 1H4a1 1 0 0 1-1-1V1a1 1 0 0 1 1-1zm.5 1.5v10h5v-10z"/></svg>
        (864) 555-0148
      </li>
      <li class="contact-item">
        <svg class="contact-icon" viewBox="0 0 14 14"><path d="M1 4c0-2 2-3 6-3s6 1 6 3v1H10V4H4v1H1zM3 6h8l2 6H1z"/></svg>
        (864) 555-0172
      </li>
      <li class="contact-item">
        <svg class="contact-icon" viewBox="0 0 14 14"><path d="M3 0h8v4H3zM1 5h12v6h-2V8H3v3H1zM4 9h6v5H4z"/></svg>
        (864) 555-0193
      </li>
      <li class="contact-item gap">
        <svg class="contact-icon" viewBox="0 0 14 14"><path d="M0 3h14v1L7 8 0 4zM0 5.5l7 4 7-4V12H0z"/></svg>
        dale@larkfieldhc.net
      </li>
      <li class="contact-item gap">
        <svg class="contact-icon" viewBox="0 0 14 14"><path d="M7 0a7 7 0 1 0 0 14A7 7 0 0 0 7 0zm-1 1.6C5 3 4.5 4.8 4.4 6.3H1.6A5.5 5.5 0 0 1 6 1.6zm2 0a5.5 5.5 0 0 1 4.4 4.7H9.6C9.5 4.8 9 3 8 1.6zM5.9 6.3C6 4.7 6.4 3.3 7 2.2c.6 1.1 1 2.5 1.1 4.1zm-4.3 1.4h2.8c.1 1.5.6 3.3 1.6 4.7a5.5 5.5 0 0 1-4.4-4.7zm4.3 0h2.2c-.1 1.6-.5 3-1.1 4.1-.6-1.1-1-2.5-1.1-4.1zm3.7 0h2.8A5.5 5.5 0 0 1 8 12.4c1-1.4 1.5-3.2 1.6-4.7z"/></svg>
        www.larkfieldhc.net
      </li>
      <li class="contact-item gap">
        <svg class="contact-icon" viewBox="0 0 14 14"><path d="M7 0a5 5 0 0 1 5 5c0 3.5-5 9-5 9S2 8.5 2 5a5 5 0 0 1 5-5zm0 3a2 2 0 1 0 0 4 2 2 0 0 0 0-4z"/></svg>
        <span>42 Marsh Hollow Road,<br>Greenwood, SC 29646</span>
      </li>
    </ul>

    <p class="services">Heating • Cooling • Plumbing • Residential • Commercial • Industrial</p>
  </section>
</body>
</html>
```